I am a surgeon that operates on gynaecological cancer. Wish a design and logo for letter head.

Design should include my name: Dr. Kiran Mudaly, qualifications: FTELSWOB, CGO. and state that I am a Gynaecological Oncologist and Advanced Laparoscopic Surgeon.
As for a logo. As all cancer is related to DNA, I think that that double helix could be used to symbolise a female shape, exaggerating the abdomen to suggest a mass.

Reason: Extended to view changes I have asked for.

```html
<!DOCTYPE html>
<html lang="en">
<head>
<meta charset="utf-8">
<title>Dr. Kiran Mudaly — Letterhead</title>
<link rel="stylesheet" href="https://fonts.googleapis.com/css2?family=Michroma&family=Oswald:wght@500&family=Roboto+Condensed:wght@400&display=swap">
<style>
  :root {
    --paper: #f5f5f5;
    --plum: #6b2c64;
    --ink: #141414;
    --text-dark: #2a2a2a;
  }
  html, body {
    margin: 0;
    padding: 0;
    overflow: hidden;
    background: var(--paper);
  }
  .letterhead {
    position: relative;
    width: 923px;
    height: 1200px;
    background: var(--paper);
    overflow: hidden;
  }
  .corner-band {
    position: absolute;
    left: 0;
    top: 0;
  }
  .brand-mark {
    position: absolute;
    left: 30px;
    top: 34px;
    width: 40px;
    height: 40px;
    border: 4px solid var(--plum);
    border-radius: 50%;
    box-sizing: border-box;
  }
  .doctor-name {
    position: absolute;
    left: 90px;
    top: 38px;
    margin: 0;
    font-family: "Michroma", sans-serif;
    font-weight: 400;
    font-size: 31px;
    line-height: 1;
    color: var(--plum);
    letter-spacing: 0.5px;
    white-space: nowrap;
  }
  .specialty {
    position: absolute;
    left: 173px;
    top: 80px;
    margin: 0;
    font-family: "Oswald", sans-serif;
    font-weight: 500;
    font-size: 13px;
    line-height: 1;
    color: var(--text-dark);
    letter-spacing: 0.6px;
    white-space: nowrap;
  }
  .qualifications {
    position: absolute;
    left: 60px;
    top: 97px;
    margin: 0;
    font-family: "Roboto Condensed", sans-serif;
    font-size: 12px;
    line-height: 1;
    color: var(--plum);
    letter-spacing: 1.4px;
    white-space: nowrap;
  }
  .rule {
    position: absolute;
    left: 0;
    width: 749px;
    height: 3px;
  }
  .rule--plum { top: 128px; background: var(--plum); }
  .rule--ink { top: 139px; background: var(--ink); }
</style>
</head>
<body>
  <main class="letterhead">
    <svg class="corner-band" width="923" height="1200" viewBox="0 0 923 1200" aria-hidden="true">
      <path class="band-top" fill="var(--plum)"
            d="M616,0 L839,0 Q875,100 923,180 L923,393 Q830,265 736,126 Q680,50 616,0 Z"/>
      <path class="band-bottom" fill="var(--ink)"
            d="M0,977 Q60,1060 100,1130 Q130,1170 168,1200 L25,1200 Q10,1175 0,1157 Z"/>
    </svg>

    <header class="masthead">
      <span class="brand-mark" aria-hidden="true"></span>
      <h1 class="doctor-name">DR. KIRAN MUDALY</h1>
      <p class="specialty">GYNAECOLOGICAL ONCOLOGIST &amp; ADVANCED LAPAROSCOPIC SURGEON</p>
      <p class="qualifications">FTELSWOB, CGO</p>
    </header>

    <div class="rule rule--plum"></div>
    <div class="rule rule--ink"></div>
  </main>
</body>
</html>
```